Business Card for Orvane Parts Wholesale supplier

Hi There! I need a new business card for our company. We are specialized in selling Orvane parts, mostly we sell new LCD screens for Telvox and Slatrons. I would like to see that back in the design.

You can find the colors and logo's on our website: www.dorvak-example.nl

Industry/Entity Type

Business

Contact Information for Business Card

My Details:
Lars Vintorp

Phone: 0031612873406
E-mail: Lars@dorvak-example.nl

Slogan: "Because Quality Matters"

Font styles to use
Sans Serif

Colors

Designer to choose colors to be used in the design.

Requirements
Must have
• A Black backside with the Dorvak logo on it. The front side should be clean with only my contact details.
• But I'm also open for something really different or awesome!
Nice to have
• Remember that we are in the parts & repairing industry, So i'll be handing those business cards mainly to repair companies. Maybe you can do something with that thought :)

```html
<!DOCTYPE html>
<html lang="en">
<head>
<meta charset="utf-8">
<title>Dorvak business card</title>
<link rel="stylesheet" href="https://fonts.googleapis.com/css2?family=Open+Sans:wdth,wght@75..100,400..800&display=swap">
<style>
  :root {
    --stage: #e9e7e3;
    --navy: #171e2a;
    --paper: #ffffff;
    --ink: #111111;
    --mark-grey: #9a9a9a;
    --photo-light: #f1f1f1;
    --photo-mid: #d6d6d6;
    --shadow: rgba(0, 0, 0, 0.18);
  }
  * { box-sizing: border-box; margin: 0; padding: 0; }
  html, body {
    width: 1200px; height: 900px; overflow: hidden;
    background: var(--stage);
    font-family: "Open Sans", Arial, sans-serif;
  }
  .canvas { position: relative; width: 1200px; height: 900px; }

  .card {
    position: absolute;
    width: 540px; height: 310px;
    box-shadow: 0 10px 28px var(--shadow);
  }

  /* Back side */
  .card--back {
    left: 70px; top: 150px;
    background: var(--navy);
    color: var(--paper);
  }
  .brand {
    display: flex; align-items: center; gap: 18px;
    font-weight: 700; letter-spacing: 1px; line-height: 1;
  }
  .brand__square { display: block; background: var(--mark-grey); }
  .card--back .brand {
    position: absolute; left: 120px; top: 92px;
    font-size: 64px;
  }
  .card--back .brand__square { width: 56px; height: 56px; }
  .tagline {
    position: absolute; left: 0; right: 0; top: 212px;
    text-align: center;
    font-size: 21px; font-weight: 600; letter-spacing: 0.3px;
  }
  .tagline__divider { margin: 0 12px; font-weight: 400; }

  /* Front side */
  .card--front {
    left: 590px; top: 440px;
    background: var(--paper);
    color: var(--ink);
  }
  .card--front .brand {
    position: absolute; left: 40px; top: 40px;
    font-size: 58px;
  }
  .card--front .brand__square { width: 50px; height: 50px; }
  .product-photo {
    position: absolute; right: 28px; top: 112px;
    width: 170px; height: 130px;
    background: linear-gradient(90deg, var(--photo-light), var(--photo-mid));
  }
  .contact { position: absolute; left: 40px; top: 166px; }
  .contact__name {
    font-size: 19px; font-weight: 600; letter-spacing: 1.6px;
    margin-bottom: 10px;
  }
  .contact__list { list-style: none; }
  .contact__item {
    display: flex; align-items: center; gap: 8px;
    font-size: 13px; line-height: 19px;
  }
  .contact__icon { width: 11px; height: 11px; fill: var(--ink); flex: none; }
  .slogan {
    position: absolute; left: 58px; top: 266px;
    font-size: 15px; font-weight: 600; font-stretch: 80%;
    letter-spacing: 0.2px;
  }
</style>
</head>
<body>
<main class="canvas">

  <section class="card card--back" aria-label="Card back">
    <div class="brand">
      <span class="brand__square"></span>
      <span class="brand__name">dorvak</span>
    </div>
    <p class="tagline">The highest quality<span class="tagline__divider">|</span>OEM parts</p>
  </section>

  <section class="card card--front" aria-label="Card front">
    <div class="brand">
      <span class="brand__square"></span>
      <span class="brand__name">dorvak</span>
    </div>

    <div class="product-photo" role="img" aria-label="Photo of a smartphone front and a replacement LCD screen assembly"></div>

    <div class="contact">
      <p class="contact__name">LARS VINTORP</p>
      <ul class="contact__list">
        <li class="contact__item">
          <svg class="contact__icon" viewBox="0 0 12 12" aria-hidden="true"><path d="M2.4 0.6 4.2 2.8 3.3 4.1C3.9 5.6 5.1 6.8 6.6 7.5L7.9 6.6 10.2 8.3 9.3 10.6C5 10.6 1.2 6.9 1 2.3Z"/></svg>
          <span>0031612873406</span>
        </li>
        <li class="contact__item">
          <svg class="contact__icon" viewBox="0 0 12 12" aria-hidden="true"><path d="M0.5 2.5H11.5V10H0.5Z M1.3 3.2 6 6.8 10.7 3.2V9.3H1.3Z" fill-rule="evenodd"/><path d="M1 3 6 6.6 11 3" fill="none" stroke="#fff" stroke-width="0.9"/></svg>
          <span>Lars@dorvak-example.nl</span>
        </li>
        <li class="contact__item">
          <svg class="contact__icon" viewBox="0 0 12 12" aria-hidden="true"><circle cx="6" cy="6" r="5.5"/><path d="M1 6H11M6 0.5C3.5 3 3.5 9 6 11.5M6 0.5C8.5 3 8.5 9 6 11.5" fill="none" stroke="#fff" stroke-width="0.8"/></svg>
          <span>www.dorvak-example.nl</span>
        </li>
      </ul>
    </div>

    <p class="slogan">BECAUSE QUALITY MATTERS</p>
  </section>

</main>
</body>
</html>
```